Digital Marketing Website Design

I need the homepage designed for my new digital marketing agency I am starting. The main goal for this homepage is to drive people to make an appointment for me to discuss their upcoming projects. Here are some examples of the layouts that I would like to emulate.
https://www.tallorchard.com/
https://www.webmerchantry.com/
https://talewick.com/
https://drmevorran.com/
https://www.neatlynestled.org/
My main focus is to attract leads that need help with running digital ads such as Chatterbook ads and Quorix Ads. I do offer other services like SEO and other things but the main focus is digital Ads.
The final design should communicate Ember Pixelry is a Digital marketing strategist building predictable revenue for small businesses through digital ads, email and marketing automation.
Target Market(s)
30-55, business owners, income 100K+, ecommerce companies, etc.
Industry/Entity Type
Digital Marketing
Number of Pages Required
2 page
Requirements
Must have
- An appealing look and feel set to drive people to make an appointment.
There needs to be a call to action button in the far right of the navigation
The same call to action in the navigation needs to be in each section on the homepage.
I need the homepage and an about us page.

```html
<!DOCTYPE html>
<html lang="en">
<head>
<meta charset="utf-8">
<title>Ember Pixelry — Digital Ads for Small Businesses</title>
<link rel="stylesheet" href="https://fonts.googleapis.com/css2?family=Roboto:wght@300;400;500;700;900&family=Open+Sans:wght@400;600&display=swap">
<style>
  :root {
    --orange: #f26522;
    --orange-light: #f7932b;
    --red: #d8361f;
    --ink: #222222;
    --text: #5c5c5c;
    --muted: #8a8a8a;
    --line: #e2e2e2;
    --paper: #ffffff;
    --soft: #f6f6f6;
    --footer: #1b1b1b;
  }
  * { box-sizing: border-box; margin: 0; padding: 0; }
  html, body { width: 1200px; height: 3104px; overflow: hidden; }
  body { font-family: "Open Sans", sans-serif; color: var(--text); background: var(--paper); position: relative; }
  .heading-font { font-family: "Roboto", sans-serif; }

  /* Header & hero */
  .hero { position: absolute; top: 0; left: 0; width: 1200px; height: 740px; overflow: hidden; }
  .hero-backdrop { position: absolute; inset: 0;
    background: linear-gradient(180deg, #f4f1ee 0%, #ece6e0 45%, #c9b8a6 62%, #8f7a68 80%, #5c4c40 100%); }
  .nav { position: absolute; top: 0; left: 0; right: 0; height: 80px; display: flex; align-items: center; padding: 0 70px 0 70px; background: rgba(255,255,255,0.85); }
  .brand { display: flex; align-items: center; gap: 10px; font-family: "Roboto", sans-serif; font-weight: 900; font-size: 26px; color: var(--ink); letter-spacing: 0.5px; }
  .brand-dot { width: 14px; height: 14px; background: var(--orange); border-radius: 50%; }
  .nav-links { margin-left: auto; display: flex; gap: 30px; list-style: none; font-family: "Roboto", sans-serif; font-size: 13px; font-weight: 500; color: var(--ink); }
  .nav-links li.active { color: var(--orange); border-bottom: 2px solid var(--orange); padding-bottom: 4px; }
  .btn { display: inline-block; font-family: "Roboto", sans-serif; font-weight: 700; font-size: 13px; text-transform: uppercase; padding: 13px 22px; border-radius: 3px; letter-spacing: 0.3px; }
  .btn-primary { background: var(--orange); color: #fff; }
  .btn-outline { background: #fff; color: var(--ink); border: 2px solid var(--ink); }
  .nav .btn { margin-left: 34px; }
  .hero-copy { position: absolute; top: 140px; left: 0; right: 0; text-align: center; }
  .hero-title { font-family: "Roboto", sans-serif; font-weight: 900; font-size: 46px; line-height: 1.1; color: var(--orange); text-transform: uppercase; }
  .hero-sub { margin: 16px auto 0; width: 640px; font-size: 16px; line-height: 1.5; color: #444; }
  .hero-actions { margin-top: 26px; display: flex; justify-content: center; gap: 18px; }
  .hero-dots { position: absolute; top: 382px; left: 0; right: 0; display: flex; justify-content: center; gap: 8px; }
  .dot { width: 12px; height: 12px; border-radius: 50%; border: 2px solid var(--orange); background: #fff; }
  .dot.on { background: var(--orange); }

  /* Featured bar */
  .featured { position: absolute; top: 740px; left: 0; width: 1200px; height: 86px; background: var(--paper); border-bottom: 1px solid var(--line); display: flex; align-items: center; padding: 0 60px; gap: 56px; }
  .featured-label { font-family: "Roboto", sans-serif; font-weight: 700; font-size: 14px; color: var(--ink); }
  .press { font-family: "Roboto", sans-serif; font-weight: 700; font-size: 26px; color: var(--ink); }
  .press.small { font-size: 14px; }

  /* Section titles */
  .section-title { display: flex; justify-content: center; align-items: center; gap: 14px; font-family: "Roboto", sans-serif; font-weight: 900; font-size: 40px; text-transform: uppercase; }
  .title-rule { width: 60px; height: 3px; background: var(--orange); margin: 14px auto 0; }

  /* How it works */
  .how { position: absolute; top: 826px; left: 0; width: 1200px; height: 594px; background: var(--paper); }
  .how .section-title { margin-top: 60px; color: var(--ink); }
  .how-intro { width: 860px; margin: 26px auto 0; text-align: center; font-size: 13px; line-height: 1.7; }
  .how-intro p + p { margin-top: 12px; }
  .steps { position: absolute; top: 352px; left: 140px; width: 1000px; display: flex; align-items: center; }
  .step { width: 280px; height: 142px; background: #fff; box-shadow: 0 3px 12px rgba(0,0,0,0.12); border-left: 4px solid var(--orange); padding: 26px 22px; font-size: 13px; line-height: 1.6; }
  .step-arrow { width: 80px; display: flex; justify-content: center; }
  .how-outro { position: absolute; top: 534px; left: 0; right: 0; text-align: center; font-size: 13px; width: 820px; margin: 0 auto; line-height: 1.6; }

  /* Testimonials */
  .reviews { position: absolute; top: 1420px; left: 0; width: 1200px; height: 840px;
    background: linear-gradient(180deg, var(--red) 0%, #e85522 55%, var(--orange-light) 100%); }
  .reviews .section-title { margin-top: 76px; color: #fff; }
  .reviews .title-rule { background: #fff; }
  .cards { position: absolute; top: 280px; left: 140px; width: 920px; display: flex; gap: 40px; }
  .card { width: 280px; background: #fff; border-radius: 3px; box-shadow: 0 4px 14px rgba(0,0,0,0.18); padding: 0 22px 26px; }
  .card-head { display: flex; align-items: center; gap: 12px; height: 60px; margin-top: -24px; }
  .avatar { width: 52px; height: 52px; border-radius: 50%; border: 3px solid #fff; background: linear-gradient(135deg, #c9a98c, #7e6452); }
  .reviewer { font-family: "Roboto", sans-serif; font-size: 13px; font-weight: 500; color: var(--ink); padding-top: 18px; }
  .stars { color: var(--orange); font-size: 12px; letter-spacing: 2px; }
  .quote-mark { font-family: "Roboto", sans-serif; font-weight: 900; font-size: 34px; color: var(--orange); line-height: 1; margin-top: 14px; }
  .card p { font-size: 12.5px; line-height: 1.7; margin-top: 4px; }
  .reviews .hero-dots { top: 752px; }
  .reviews .dot { border-color: #fff; background: transparent; }
  .reviews .dot.on { background: #fff; }

  /* Contact */
  .contact { position: absolute; top: 2260px; left: 0; width: 1200px; height: 600px; background: var(--paper); overflow: hidden; }
  .contact-skyline { position: absolute; left: 0; right: 0; bottom: 0; height: 150px; background: linear-gradient(180deg, rgba(230,230,230,0) 0%, #ececec 100%); }
  .contact .section-title { margin-top: 70px; color: var(--ink); }
  .contact-form { position: absolute; top: 208px; left: 140px; width: 620px; display: grid; grid-template-columns: 280px 320px; column-gap: 20px; }
  .field-col { display: flex; flex-direction: column; gap: 14px; }
  .field { height: 48px; border: 1px solid #d5d5d5; padding: 14px 12px; font-size: 12px; color: var(--muted); background: #fff; }
  .field.message { height: 234px; }
  .contact-form .btn { margin-top: 22px; width: 120px; text-align: center; }
  .contact-info { position: absolute; top: 208px; left: 800px; width: 320px; list-style: none; }
  .contact-info li { display: flex; align-items: center; gap: 16px; margin-bottom: 26px; font-size: 13px; color: var(--ink); }
  .info-icon { width: 40px; height: 40px; border-radius: 50%; background: var(--orange); display: flex; align-items: center; justify-content: center; flex-shrink: 0; }
  .phone-number { font-family: "Roboto", sans-serif; font-weight: 700; font-size: 20px; }
  .socials { display: flex; gap: 10px; margin-left: 56px; }
  .social { width: 30px; height: 30px; border-radius: 50%; border: 1px solid #9bb3c9; }

  /* Footer */
  .footer { position: absolute; top: 2860px; left: 0; width: 1200px; height: 244px; background: var(--footer); text-align: center; color: #cfcfcf; }
  .footer .brand { justify-content: center; color: #fff; margin-top: 58px; }
  .footer-links { margin-top: 44px; font-size: 13px; display: flex; justify-content: center; gap: 10px; list-style: none; }
  .footer-links li + li::before { content: "|"; margin-right: 10px; color: #777; }
  .copyright { margin-top: 12px; font-size: 12px; color: #9a9a9a; }
</style>
</head>
<body>

<header class="hero">
  <div class="hero-backdrop" role="img" aria-label="Photo of a row of business people sitting against a light brick wall, looking at phones and laptops"></div>
  <nav class="nav">
    <div class="brand"><span class="brand-dot"></span>EMBER PIXELRY</div>
    <ul class="nav-links">
      <li class="active">HOME</li>
      <li>ABOUT US</li>
      <li>OUR SERVICES</li>
      <li>BLOG</li>
      <li>CONTACT US</li>
    </ul>
    <span class="btn btn-primary">Schedule Appointment</span>
  </nav>
  <div class="hero-copy">
    <h1 class="hero-title">We built profitable ad<br>campaigns for small businesses</h1>
    <p class="hero-sub">The selling system that brings in predictable revenue through digital ads, email, and marketing automation.</p>
    <div class="hero-actions">
      <span class="btn btn-outline">Free Chatterbook Ads Checklist</span>
      <span class="btn btn-primary">Schedule Appointment</span>
    </div>
  </div>
  <div class="hero-dots"><span class="dot on"></span><span class="dot"></span><span class="dot"></span><span class="dot"></span></div>
</header>

<section class="featured">
  <span class="featured-label">FEATURED IN:</span>
  <span class="press small">Founder Weekly</span>
  <span class="press">The Daily Ledger</span>
  <span class="press">HOURLY</span>
  <span class="press">Fortbright</span>
  <span class="press">Venturo</span>
</section>

<section class="how">
  <h2 class="section-title">
    <svg width="26" height="34" viewBox="0 0 26 34"><path d="M13 1 C16 9 24 13 24 22 A11 11 0 0 1 2 22 C2 16 6 13 8 9 C9 14 11 15 12 16 C14 11 14 6 13 1 Z" fill="#f26522"/></svg>
    How It Works
  </h2>
  <div class="title-rule"></div>
  <div class="how-intro">
    <p>At Ember Pixelry we know that you want to run a profitable business. To do that, you need a strong system that can predictably bring in sales, even in slow times. The problem is there is so much out there to wade through and so many people telling you what to do, which leaves you feeling frustrated, lost and stressed out. We believe that businesses with great products should get the customers they deserve.</p>
    <p>We understand this frustration, which is why we are here to help you move through the noise and create a system that works.</p>
  </div>
  <div class="steps">
    <div class="step">Schedule an appointment to go through the basics of what you need and to find out if we are a good fit to work together.</div>
    <div class="step-arrow"><svg width="40" height="20" viewBox="0 0 40 20"><path d="M2 10 H34 M26 3 L35 10 L26 17" stroke="#f26522" stroke-width="3" fill="none"/></svg></div>
    <div class="step">Work with our team to build out your customer journey and selling system.</div>
    <div class="step-arrow"><svg width="40" height="20" viewBox="0 0 40 20"><path d="M2 10 H34 M26 3 L35 10 L26 17" stroke="#f26522" stroke-width="3" fill="none"/></svg></div>
    <div class="step">Execute and enjoy the extra revenue!</div>
  </div>
  <p class="how-outro">So, schedule your appointment today. And in the meantime, check out our Chatterbook ads checklist, so you can stop any poor running campaigns and fill in the gaps where they are needed.</p>
</section>

<section class="reviews">
  <h2 class="section-title">
    <svg width="26" height="34" viewBox="0 0 26 34"><path d="M13 1 C16 9 24 13 24 22 A11 11 0 0 1 2 22 C2 16 6 13 8 9 C9 14 11 15 12 16 C14 11 14 6 13 1 Z" fill="#ffffff"/></svg>
    What Others Are Saying...
  </h2>
  <div class="title-rule"></div>
  <div class="cards">
    <article class="card">
      <div class="card-head"><div class="avatar" role="img" aria-label="Client portrait"></div><div class="reviewer">Dana - Ember Pixelry<div class="stars">★★★★★</div></div></div>
      <div class="quote-mark">“</div>
      <p>Lorem ipsum dolor sit amet, conse adipiscing elit, sed do eiusmod tempor incididunt ut labore et dolore magna aliqua. Ut enim ad minim veniam, quis nostrud exercitation ullamco laboris nisi ut aliquip ex ea commodo consequat. Duis aute irure dolor.</p>
    </article>
    <article class="card">
      <div class="card-head"><div class="avatar" role="img" aria-label="Client portrait"></div><div class="reviewer">Dana - Ember Pixelry<div class="stars">★★★★★</div></div></div>
      <div class="quote-mark">“</div>
      <p>Lorem ipsum dolor sit amet, conse adipiscing elit, sed do eiusmod tempor incididunt ut labore et dolore magna aliqua. Ut enim ad minim veniam, quis nostrud exercitation ullamco laboris nisi ut aliquip ex ea commodo consequat. Duis aute irure dolor.</p>
    </article>
    <article class="card">
      <div class="card-head"><div class="avatar" role="img" aria-label="Client portrait"></div><div class="reviewer">Dana - Ember Pixelry<div class="stars">★★★★★</div></div></div>
      <div class="quote-mark">“</div>
      <p>Lorem ipsum dolor sit amet, conse adipiscing elit, sed do eiusmod tempor incididunt ut labore et dolore magna aliqua. Ut enim ad minim veniam, quis nostrud exercitation ullamco laboris nisi ut aliquip ex ea commodo consequat. Duis aute irure dolor.</p>
    </article>
  </div>
  <div class="hero-dots"><span class="dot on"></span><span class="dot"></span><span class="dot"></span><span class="dot"></span></div>
</section>

<section class="contact">
  <div class="contact-skyline" role="img" aria-label="Faint city skyline illustration"></div>
  <h2 class="section-title">
    <svg width="26" height="34" viewBox="0 0 26 34"><path d="M13 1 C16 9 24 13 24 22 A11 11 0 0 1 2 22 C2 16 6 13 8 9 C9 14 11 15 12 16 C14 11 14 6 13 1 Z" fill="#f26522"/></svg>
    Contact Us
  </h2>
  <div class="title-rule"></div>
  <form class="contact-form">
    <div class="field-col">
      <div class="field">First name</div>
      <div class="field">Last Name</div>
      <div class="field">Email</div>
      <div class="field">Phone</div>
    </div>
    <div class="field-col">
      <div class="field message">Message</div>
    </div>
    <span class="btn btn-primary">Submit</span>
  </form>
  <ul class="contact-info">
    <li><span class="info-icon"><svg width="16" height="20" viewBox="0 0 16 20"><path d="M8 1 A7 7 0 0 1 15 8 C15 13 8 19 8 19 C8 19 1 13 1 8 A7 7 0 0 1 8 1 Z" fill="#fff"/><circle cx="8" cy="8" r="2.6" fill="#f26522"/></svg></span><span>Ember Pixelry<br>48 Alder Lane Norwood, MA</span></li>
    <li><span class="info-icon"><svg width="18" height="18" viewBox="0 0 18 18"><path d="M4 1 L7 5 L5 7 C6 10 8 12 11 13 L13 11 L17 14 L15 17 C8 17 1 10 1 3 Z" fill="#fff"/></svg></span><span class="phone-number">555-0184-2210</span></li>
    <li><span class="info-icon"><svg width="18" height="14" viewBox="0 0 18 14"><rect x="1" y="1" width="16" height="12" fill="#fff"/><path d="M1 1 L9 8 L17 1" stroke="#f26522" stroke-width="1.6" fill="none"/></svg></span><span>info@emberpixelry.com</span></li>
  </ul>
  <div class="socials" style="position:absolute;top:424px;left:800px;">
    <span class="social"></span><span class="social"></span><span class="social"></span><span class="social"></span>
  </div>
</section>

<footer class="footer">
  <div class="brand"><span class="brand-dot"></span>EMBER PIXELRY</div>
  <ul class="footer-links">
    <li>Home</li><li>About</li><li>Services</li><li>Case studies</li><li>Contact</li><li>Terms of Service</li><li>Privacy Policy</li>
  </ul>
  <p class="copyright">Copyright 2020 Ember Pixelry. All rights reserved.</p>
</footer>

</body>
</html>
```